Digital Marketing Website Design

I need the homepage designed for my new digital marketing agency I am starting. The main goal for this homepage is to drive people to make an appointment for me to discuss their upcoming projects. Here are some examples of the layouts that I would like to emulate.
https://www.tallmarsh.com/
https://www.quillforge.com/
https://pebblenook.com/
https://drvenholt.com/
https://www.quietlyrooted.org/
My main focus is to attract leads that need help with running digital ads such as Chatterly ads and Finder Promos. I do offer other services like SEO and other things but the main focus is digital Ads.
The final design should communicate Orchid Digital is a Digital marketing strategist building predictable revenue for small businesses through digital ads, email and marketing automation.
Target Market(s)
30-55, business owners, income 100K+, ecommerce companies, etc.
Industry/Entity Type
Digital Marketing
Number of Pages Required
2 page
Font styles to use
Requirements
Must have
- An appealing look and feel set to drive people to make an appointment.
Logo
There needs to be a call to action button in the far right of the navigation
The same call to action in the navigation needs to be in each section on the homepage.
I need the homepage and an about us page.

```html
<!DOCTYPE html>
<html lang="en">
<head>
<meta charset="utf-8">
<title>Orchid Digital — Home</title>
<link rel="stylesheet" href="https://fonts.googleapis.com/css2?family=Michroma&family=Montserrat:ital,wght@0,400;0,500;0,600;0,700;1,400&display=swap">
<style>
:root{
  --orange:#f26522;
  --orange-2:#ff8a00;
  --orange-3:#f47a12;
  --ink:#111111;
  --text:#222222;
  --white:#ffffff;
  --sky:#7fd3f2;
  --sky-2:#3fb6e6;
  --footer:#1f1f23;
  --footer-text:#9a9aa2;
  --badge:#b9b9b9;
}
*{box-sizing:border-box;margin:0;padding:0}
html,body{width:1200px;height:2563px;overflow:hidden}
body{position:relative;font-family:"Montserrat",Arial,sans-serif;color:var(--text);background:var(--white)}
.abs{position:absolute}
.display{font-family:"Michroma","Montserrat",sans-serif;text-transform:uppercase;letter-spacing:.5px}
.btn{display:inline-block;background:var(--orange);color:var(--white);font-weight:600;font-size:12px;text-transform:uppercase;text-decoration:none;text-align:center;border-radius:2px}

/* hero */
.hero{left:0;top:0;width:1200px;height:775px;overflow:hidden}
.hero-photo{left:0;top:0;width:1200px;height:775px;background:
  radial-gradient(ellipse 420px 520px at 900px 380px,#8a7a6d 0%,#b7aba0 40%,transparent 75%),
  radial-gradient(ellipse 380px 240px at 380px 640px,#d9d6d2 0%,transparent 70%),
  linear-gradient(180deg,#ffffff 0%,#f5f3f0 45%,#e9e4dd 80%,#d8d0c4 100%)}
.logo{font-family:"Montserrat",sans-serif;font-weight:700;font-size:25px;color:var(--orange);letter-spacing:-.5px;display:flex;align-items:center;gap:8px}
.logo-dot{width:14px;height:14px;border-radius:50%;background:var(--orange)}
.nav{left:678px;top:60px;display:flex;gap:40px;font-size:12px;font-weight:500;text-transform:uppercase;color:var(--ink)}
.nav .active{color:var(--orange)}
.nav-cta{left:940px;top:49px;width:187px;height:37px;line-height:37px}
.hero-title{left:94px;top:164px;width:620px;font-size:33px;line-height:41px;color:var(--ink)}
.hero-sub{left:95px;top:296px;width:400px;font-size:13px;line-height:22px;color:var(--ink)}
.hero-cta{left:94px;top:369px;width:187px;height:37px;line-height:37px}

/* badges */
.badges{left:0;top:775px;width:1200px;height:144px;display:flex;align-items:center;justify-content:center;gap:0}
.badge{position:absolute;background:var(--badge)}

/* how it works */
.how{left:0;top:919px;width:1200px;height:616px;background:linear-gradient(180deg,var(--orange-3) 0%,var(--orange-2) 100%);overflow:hidden}
.how-photo{left:755px;top:30px;width:300px;height:586px;border-radius:140px 140px 0 0;background:linear-gradient(180deg,#e9b98a 0%,#c9895a 25%,#262220 45%,#121212 100%)}
.how-deco{left:520px;top:0;width:680px;height:616px;background:radial-gradient(ellipse at 60% 40%,rgba(255,255,255,.10),transparent 70%)}
.how-title{left:88px;top:94px;font-size:31px;color:var(--white)}
.how-body{left:89px;top:150px;width:610px;font-size:12.5px;line-height:22.3px;color:var(--white)}
.how-body p{margin-bottom:22px}
.how-body strong{font-weight:700}
.steps{list-style:none;margin-bottom:22px}
.steps li{position:relative;padding-left:31px}
.steps svg{position:absolute;left:0;top:5px}

/* testimonials */
.saying{left:0;top:1535px;width:1200px;height:645px;background:linear-gradient(180deg,var(--sky) 0%,var(--sky-2) 100%);overflow:hidden}
.saying-photo{left:62px;top:10px;width:420px;height:635px;border-radius:200px 200px 0 0;background:linear-gradient(180deg,#e8c58c 0%,#f1d6bf 25%,#f4f1ee 55%,#e7e2dc 80%,#3c4a66 100%)}
.saying-title{left:0;top:149px;width:1200px;text-align:center;font-size:32px;color:var(--ink)}
.saying-sub{left:0;top:193px;width:1200px;text-align:center;font-size:12.5px;color:var(--ink)}
.card{top:273px;width:320px;height:176px;background:var(--white);padding:20px 20px 0 19px}
.card q{display:block;font-style:italic;font-size:12.5px;line-height:22.3px;color:var(--text);quotes:none;width:282px}
.card .name{position:absolute;left:19px;top:106px;font-weight:600;font-size:17px;color:var(--ink)}
.card .role{position:absolute;left:19px;top:132px;font-size:12.5px;color:var(--ink)}
.avatar{position:absolute;left:231px;top:89px;width:64px;height:64px;border-radius:50%}
.arrows{left:585px;top:474px;display:flex;gap:14px}

/* footer */
.footer{left:0;top:2180px;width:1200px;height:383px;background:var(--footer);color:var(--footer-text);font-size:12.5px}
.footer .logo{color:var(--orange)}
.f-col-title{color:var(--white);font-weight:600;font-size:12.5px}
.footer a{color:var(--footer-text);text-decoration:none}
.f-contact{display:flex;align-items:center;gap:14px;color:var(--footer-text)}
.f-contact.mail{color:var(--white)}
.social{left:997px;top:2330px;display:flex;gap:14px}
.social span{width:21px;height:21px;border-radius:50%;background:var(--white)}
.copyright{left:0;top:2519px;width:1200px;text-align:center;font-size:12.5px;color:var(--footer-text)}
</style>
</head>
<body>

<!-- hero -->
<section class="hero abs">
  <div class="hero-photo abs" role="img" aria-label="Smiling bearded man in glasses and a checked shirt typing on a laptop at a bright desk"></div>
  <a class="logo abs" style="left:90px;top:52px" href="#"><span class="logo-dot"></span>ORCHID DIGITAL</a>
  <nav class="nav abs">
    <a class="active">Home</a><a>About</a><a>Contact</a>
  </nav>
  <a class="btn nav-cta abs" href="#">Schedule Appointment</a>
  <h1 class="hero-title display abs">We Built Profitable Ad Campaigns for Small Businesses</h1>
  <p class="hero-sub abs">The selling system that brings in Predictable revenue through digital ads, email, and marketing automation.</p>
  <a class="btn hero-cta abs" href="#">Schedule Appointment</a>
</section>

<!-- badges -->
<section class="badges abs" aria-label="Memberships and listings">
  <span class="badge" style="left:176px;top:42px;width:62px;height:62px;border-radius:50%"></span>
  <span class="badge" style="left:310px;top:40px;width:150px;height:62px;border-radius:4px"></span>
  <span class="badge" style="left:554px;top:42px;width:55px;height:58px;border-radius:6px"></span>
  <span class="badge" style="left:706px;top:38px;width:64px;height:64px;border-radius:2px"></span>
  <span class="badge" style="left:866px;top:40px;width:150px;height:62px;border-radius:4px"></span>
</section>

<!-- how it works -->
<section class="how abs">
  <div class="how-deco abs" role="img" aria-label="Faint line icons for communication, social media, account growth and groups"></div>
  <div class="how-photo abs" role="img" aria-label="Smiling woman with long hair in a black top, arms crossed"></div>
  <h2 class="how-title display abs">How It Works</h2>
  <div class="how-body abs">
    <p>At Orchid Digital we know that you want to have a profitable business. In order to do that, you need a strong system that can predictably bring in sales even in bad times. The problem is there is so much out there to wade through and so many people telling you what you should do which makes you feel frustrated, lost, and flat out stressed out. We believe that businesses with great products should get the customer. We understand the frustration which is why we are here to help you maneuver through the minutiae and create a system that flat out works.</p>
    <p><strong>Here’s how we do it:</strong></p>
    <ul class="steps">
      <li><svg width="14" height="14" viewBox="0 0 14 14" fill="none" stroke="#fff" stroke-width="1.3"><path d="M12.5 6.4A5.6 5.6 0 1 1 9.6 1.8"/><path d="M4.3 6.6l2.3 2.3 6-6.2"/></svg>Schedule an appointment to go through the basics of what you need and to find out if we are a good fit to work together.</li>
      <li><svg width="14" height="14" viewBox="0 0 14 14" fill="none" stroke="#fff" stroke-width="1.3"><path d="M12.5 6.4A5.6 5.6 0 1 1 9.6 1.8"/><path d="M4.3 6.6l2.3 2.3 6-6.2"/></svg>Work with our team to build out your customer journey and selling system</li>
      <li><svg width="14" height="14" viewBox="0 0 14 14" fill="none" stroke="#fff" stroke-width="1.3"><path d="M12.5 6.4A5.6 5.6 0 1 1 9.6 1.8"/><path d="M4.3 6.6l2.3 2.3 6-6.2"/></svg>Execute and enjoy the extra revenue!</li>
    </ul>
    <p>So, schedule your appointment today. And in the meantime, checkout our Chatterly ads checklist. So you can stop any poor running campaigns and fill in the gaps where they are needed.</p>
  </div>
</section>

<!-- testimonials -->
<section class="saying abs">
  <div class="saying-photo abs" role="img" aria-label="Laughing blonde woman in a white shirt holding a laptop"></div>
  <h2 class="saying-title display abs">What Others Are Saying</h2>
  <p class="saying-sub abs">At Orchid Digital we know that you want to have a profitable business.</p>

  <article class="card abs" style="left:90px">
    <q>Lorem Ipsum is simply dummy text of the printing and typesetting industry. Lorem Ipsum has been the industry's</q>
    <span class="name">Name Here</span><span class="role">Satsfied Client</span>
    <span class="avatar" role="img" aria-label="Client portrait" style="background:linear-gradient(180deg,#e6cfa6,#8fb8cf)"></span>
  </article>
  <article class="card abs" style="left:442px">
    <q>Lorem Ipsum is simply dummy text of the printing and typesetting industry. Lorem Ipsum has been the industry's</q>
    <span class="name">Name Here</span><span class="role">Satsfied Client</span>
    <span class="avatar" role="img" aria-label="Client portrait" style="background:linear-gradient(180deg,#f58a1f,#c0602a)"></span>
  </article>
  <article class="card abs" style="left:803px">
    <q>Lorem Ipsum is simply dummy text of the printing and typesetting industry. Lorem Ipsum has been the industry's</q>
    <span class="name">Name Here</span><span class="role">Satsfied Client</span>
    <span class="avatar" role="img" aria-label="Client portrait" style="background:linear-gradient(180deg,#cfcfcf,#5a5a5a)"></span>
  </article>

  <div class="arrows abs">
    <svg width="14" height="16" viewBox="0 0 14 16" fill="none" stroke="#111" stroke-width="1.6"><path d="M10 2L4 8l6 6"/></svg>
    <svg width="14" height="16" viewBox="0 0 14 16" fill="none" stroke="#111" stroke-width="1.6"><path d="M4 2l6 6-6 6"/></svg>
  </div>
</section>

<!-- footer -->
<footer class="footer abs">
  <a class="logo abs" style="left:89px;top:58px" href="#"><span class="logo-dot"></span>ORCHID DIGITAL</a>
  <p class="abs" style="left:89px;top:132px;line-height:22px">812 Linden Crest Ave • Fairhaven, Oregon 97301<br>Phone: 555.201.4400 • Fax: 555.201.4411</p>
  <div class="f-contact abs" style="left:89px;top:2373px;top:193px">
    <svg width="18" height="16" viewBox="0 0 18 16" fill="#fff"><path d="M3 1l3 0 1.5 4-2 1.5c1 2 2.5 3.5 4.5 4.5L11.5 9l4 1.5v3c0 1-1 1.5-2 1.5C7 15 1.5 9 1.5 3c0-1 .5-2 1.5-2z"/></svg>
    <span>(555) 318-2290</span>
  </div>
  <div class="f-contact mail abs" style="left:89px;top:222px">
    <svg width="18" height="14" viewBox="0 0 18 14" fill="#fff"><path d="M0 1h18v12H0z"/><path d="M0 1l9 7 9-7" fill="none" stroke="#1f1f23" stroke-width="1.4"/></svg>
    <span>hello@orchiddigital.com</span>
  </div>

  <h3 class="f-col-title abs" style="left:472px;top:66px">Pages</h3>
  <a class="abs" style="left:474px;top:110px">Home</a>
  <a class="abs" style="left:474px;top:139px">About</a>
  <a class="abs" style="left:474px;top:168px">Services</a>
  <a class="abs" style="left:474px;top:196px">Resources</a>
  <a class="abs" style="left:571px;top:110px">Blog</a>
  <a class="abs" style="left:571px;top:139px">Contact</a>

  <h3 class="f-col-title abs" style="left:729px;top:66px">Useful Links</h3>
  <a class="abs" style="left:729px;top:111px">flagship content /case studies</a>
  <a class="abs" style="left:729px;top:139px">social properties</a>
  <a class="abs" style="left:729px;top:167px">miscellaneous information</a>
</footer>
<div class="social abs" aria-label="Social links"><span></span><span></span><span></span></div>
<p class="copyright abs">Copyright © 2020 Orchid Digital &nbsp;|&nbsp; Terms of Service &nbsp;|&nbsp; Privacy Policy</p>

</body>
</html>
```